Harbor Sushi & Steak Dinner Menu

I'm looking for a MENU design with a particular feel. I want to have a base template made that I can then use for future alterations to the menu; ie I can go in and change out different entrees as the menu changes but the template will remain the same. (Ideally it would be in an Apple Pages format.). Also ideally - dinner menu will occupy 2 pages 8.5 x 11. The restaurant's name is Harbor. It is a MODERN steak house that will also feature Sushi, a Raw Bar, Exquisite Cocktails and a sophisticated nightlife crowd. I have attached our LOGO, a secondary logo that we will be featuring throughout the project including on the menu cover (the gold U). Finally - I have attached the content that we would like to see. AGAIN - I REITERATE: High end dining and lounge atmosphere. A couple of restaurants / menus that I love are Morvendel in NYC and Pellucid Steakhouse in Long Island NY. Please do not duplicate - just trying to offer some suggestions.

Requirements
Must have
• A sophisticated and elegant feel without being stuffy or old.

```html
<!DOCTYPE html>
<html lang="en">
<head>
<meta charset="utf-8">
<title>Harbor Sushi &amp; Steak — Dinner Menu</title>
<link rel="stylesheet" href="https://fonts.googleapis.com/css2?family=Nunito+Sans:ital,wght@0,400;0,600;1,400&family=Josefin+Sans:wght@400&display=swap">
<style>
  :root {
    --backdrop: #d9d9d9;
    --paper: #ffffff;
    --gold: #d4bb6e;
    --gold-faint: #f6f1e2;
    --red: #c8202f;
  }
  * { margin: 0; padding: 0; box-sizing: border-box; }
  html, body {
    width: 1200px; height: 750px; overflow: hidden;
    background: var(--backdrop);
  }
  .spread { position: relative; width: 1200px; height: 750px; }
  .page {
    position: absolute; top: 74px; width: 464px; height: 601px;
    background: var(--paper); overflow: hidden;
  }
  .page--left { left: 136px; }
  .page--right { left: 600px; }
  .frame {
    position: absolute; left: 42px; top: 85px; width: 380px; height: 477px;
    border: 2px solid var(--gold);
  }
  .wordmark {
    position: absolute; left: 0; right: 0; top: 56px; text-align: center;
  }
  .wordmark span {
    display: inline-block; background: var(--paper); padding: 0 10px;
    font-family: "Josefin Sans", sans-serif; font-size: 21px;
    letter-spacing: 6px; color: var(--gold); line-height: 26px;
  }
  .section-title {
    position: absolute; left: 0; right: 0; top: 152px; text-align: center;
    font-family: "Nunito Sans", sans-serif; font-size: 16px; font-weight: 400;
    letter-spacing: 1px; color: var(--gold);
  }
  .menu-list { position: absolute; left: 77px; width: 315px; list-style: none; }
  .page--right .menu-list { width: 314px; }
  .menu-item { position: absolute; left: 0; width: 100%; }
  .item-name {
    font-family: "Nunito Sans", sans-serif; font-size: 12px; font-weight: 400;
    font-variant: small-caps; letter-spacing: .4px; color: var(--red);
    line-height: 12px; font-size: 13px;
  }
  .item-desc {
    display: flex; align-items: baseline;
    font-family: "Nunito Sans", sans-serif; font-style: italic;
    font-size: 8.5px; color: var(--red); line-height: 11px;
  }
  .item-desc .leader {
    flex: 1; height: 2px; margin-left: 3px;
    background-image: radial-gradient(circle, var(--red) 0.6px, transparent 0.8px);
    background-size: 5.4px 2px; background-repeat: repeat-x;
  }
  .art-corner {
    position: absolute; left: 326px; top: 97px; width: 78px; height: 60px;
    background: var(--gold); border-radius: 6px;
  }
  .art-backdrop {
    position: absolute; left: 124px; top: 319px; width: 340px; height: 282px;
    background: linear-gradient(160deg, var(--gold-faint), #f8f4ea 70%, #fbf8f1);
  }
</style>
</head>
<body>
<main class="spread">

  <section class="page page--left">
    <div class="frame"></div>
    <div class="wordmark"><span>HARBOR</span></div>
    <div class="art-corner" role="img" aria-label="Illustration of two sushi rolls with chopsticks"></div>
    <h2 class="section-title">SUSHI SASHIMI</h2>
    <ul class="menu-list" style="top:0">
      <li class="menu-item" style="top:188px"><div class="item-name">Toro</div><div class="item-desc">blue fin tuna belly (gf).<span class="leader"></span></div></li>
      <li class="menu-item" style="top:222px"><div class="item-name">Unagi</div><div class="item-desc">fresh water eel (gf).<span class="leader"></span></div></li>
      <li class="menu-item" style="top:256px"><div class="item-name">Ebi</div><div class="item-desc">cooked shrimp (gf)<span class="leader"></span></div></li>
      <li class="menu-item" style="top:290px"><div class="item-name">Sake</div><div class="item-desc">salmon (gf).<span class="leader"></span></div></li>
      <li class="menu-item" style="top:324px"><div class="item-name">Hamachi</div><div class="item-desc">yellowtail (gf)<span class="leader"></span></div></li>
      <li class="menu-item" style="top:363px"><div class="item-name">Madai</div><div class="item-desc">red snapper (gf).<span class="leader"></span></div></li>
      <li class="menu-item" style="top:402px"><div class="item-name">Uni</div><div class="item-desc">sea urchin (gf)<span class="leader"></span></div></li>
      <li class="menu-item" style="top:441px"><div class="item-name">Maguro</div><div class="item-desc">tuna (gf).<span class="leader"></span></div></li>
      <li class="menu-item" style="top:481px"><div class="item-name">Hirame</div><div class="item-desc">fluke (gf).<span class="leader"></span></div></li>
    </ul>
  </section>

  <section class="page page--right">
    <div class="art-backdrop" role="img" aria-label="Large faint illustration of sushi rolls and chopsticks"></div>
    <div class="frame"></div>
    <div class="wordmark"><span>HARBOR</span></div>
    <h2 class="section-title">CLASSIC ROLLS</h2>
    <ul class="menu-list" style="top:0">
      <li class="menu-item" style="top:222px"><div class="item-name">Yellowtail</div><div class="item-desc">inside out roll with scallions (gf)<span class="leader"></span></div></li>
      <li class="menu-item" style="top:256px"><div class="item-name">Spicy Tuna or Salmon or Yellowtail</div><div class="item-desc">spicy mayo.<span class="leader"></span></div></li>
      <li class="menu-item" style="top:290px"><div class="item-name">California</div><div class="item-desc">crab meat, cucumber and avocado (gf).<span class="leader"></span></div></li>
      <li class="menu-item" style="top:324px"><div class="item-name">Vegetable</div><div class="item-desc">avocado, cucumber, asparagus and pickled reddish (gf).<span class="leader"></span></div></li>
      <li class="menu-item" style="top:358px"><div class="item-name">Spider</div><div class="item-desc">soft shell crab and avocado with eel sauce<span class="leader"></span></div></li>
      <li class="menu-item" style="top:397px"><div class="item-name">Shrimp Tempura</div><div class="item-desc">deep fried tempura shrimp and eel sauce.<span class="leader"></span></div></li>
      <li class="menu-item" style="top:436px"><div class="item-name">Alaskan</div><div class="item-desc">salmon and avocado (gf)<span class="leader"></span></div></li>
    </ul>
  </section>

</main>
</body>
</html>
```